Virtual Reality immersive experiences

Print ad 8.5" X 11"
Advertising to have people come rent time in our virtual reality room.
Fun for all ages
Unique experience
Immersive experience into 3D world
Escape reality
Be at heart of action - bottom of the ocean, travel the world, fight the invaders, solve the mystery and so much more
System used is Brelvo Optra
Dedicated room
Family friendly
$24 half hour
$40 per hour
Updates

Industry/Entity Type

Advertising

Requirements
Must have
• Be fun looking
• Eye catching
• Great pictures of VR experiences
• Pricing is $24 / 30 minutes and $40 / 1 hour
• Our location: 587 Larch Avenue, Three Hills, Alberta
• Our contact: 403-618-2093
• I have attached TERMALDO Technology Solutions logo which should be somewhere on the ad.
Nice to have
• could use phrases like: travel the world, explore the ocean depths, fight the invaders, visit the carnival

```html
<!DOCTYPE html>
<html lang="en">
<head>
<meta charset="utf-8">
<title>Virtual Reality Immersive Experiences</title>
<link href="https://fonts.googleapis.com/css2?family=Audiowide&family=Josefin+Sans:wght@700&display=swap" rel="stylesheet">
<style>
  :root {
    --bg: #3f0e74;
    --frame: #000000;
    --neon: #7f9cff;
    --neon-glow: #4f6cff;
    --accent: #6f8df5;
    --white: #ffffff;
    --tab: #0a7fe0;
    --line: #5a4fc8;
    --brand: #2f9bd8;
  }
  * { margin: 0; padding: 0; box-sizing: border-box; }
  html, body { width: 927px; height: 1200px; overflow: hidden; background: var(--bg); }
  .ad {
    position: relative; width: 927px; height: 1200px; overflow: hidden;
    background: var(--bg);
    font-family: "Josefin Sans", sans-serif; color: var(--white);
  }
  .edge-lines { position: absolute; inset: 0; }
  .headline {
    position: absolute; left: 0; width: 927px; text-align: center;
    font-family: "Audiowide", sans-serif; color: #2a1a8a;
    -webkit-text-stroke: 2px var(--neon);
    text-shadow: 0 0 6px var(--neon-glow), 0 0 14px var(--neon-glow);
    text-transform: uppercase; white-space: nowrap;
  }
  .headline--main { top: 44px; font-size: 84px; letter-spacing: 3px; }
  .headline--sub { top: 138px; font-size: 45px; letter-spacing: 2px; -webkit-text-stroke-width: 1.5px; }
  .gallery {
    position: absolute; left: 142px; top: 216px; width: 643px; height: 478px;
    background: var(--frame);
  }
  .shot { position: absolute; }
  .headings, .features, .pricing, .price-line, .address, .contact, .brand { position: absolute; text-transform: uppercase; }
  .headings { left: 106px; top: 718px; font-size: 48px; color: var(--accent); }
  .features { left: 106px; top: 778px; list-style: none; font-size: 19px; line-height: 25.6px; }
  .pricing { left: 108px; top: 1022px; font-size: 44px; color: var(--accent); }
  .price-line { left: 108px; top: 1070px; font-size: 29px; }
  .address { left: 109px; top: 1117px; font-size: 17px; line-height: 20px; }
  .contact { left: 368px; top: 1137px; font-size: 17px; }
  .contact .label { color: var(--accent); }
  .brand { left: 672px; top: 1118px; width: 176px; text-align: right; color: var(--brand); font-size: 17px; line-height: 20px; }
  .brand small { font-size: 9px; letter-spacing: 1px; display: block; line-height: 12px; }
</style>
</head>
<body>
<main class="ad">
  <svg class="edge-lines" width="927" height="1200" viewBox="0 0 927 1200" aria-hidden="true">
    <g stroke="var(--line)" stroke-width="1" fill="none">
      <polyline points="60,0 0,160"/>
      <polyline points="0,215 102,406"/>
      <polyline points="0,200 110,400 110,460 0,690"/>
      <polyline points="102,452 0,700"/>
      <polyline points="0,745 20,1200"/>
      <polyline points="867,0 927,160"/>
      <polyline points="927,215 818,406"/>
      <polyline points="927,200 810,400 810,460 927,690"/>
      <polyline points="818,452 927,700"/>
      <polyline points="927,745 907,1200"/>
    </g>
    <g fill="var(--tab)">
      <rect x="0" y="166" width="10" height="46"/>
      <rect x="102" y="406" width="9" height="46"/>
      <rect x="0" y="696" width="10" height="44"/>
      <rect x="917" y="166" width="10" height="46"/>
      <rect x="810" y="406" width="9" height="46"/>
      <rect x="917" y="696" width="10" height="44"/>
    </g>
    <g fill="#000">
      <rect x="0" y="0" width="60" height="10"/>
      <rect x="867" y="0" width="60" height="10"/>
      <rect x="0" y="1190" width="60" height="10"/>
      <rect x="867" y="1190" width="60" height="10"/>
    </g>
  </svg>

  <h1 class="headline headline--main">Virtual Reality</h1>
  <h2 class="headline headline--sub">Immersive Experiences</h2>

  <section class="gallery">
    <div class="shot" role="img" aria-label="Players with headsets battling a green ghost" style="left:14px;top:14px;width:182px;height:112px;background:linear-gradient(135deg,#3a2a28,#1c1412 60%,#3d6a2a)"></div>
    <div class="shot" role="img" aria-label="Whales swimming in the deep ocean" style="left:213px;top:14px;width:199px;height:112px;background:linear-gradient(160deg,#2f6fb8,#0d2e6a)"></div>
    <div class="shot" role="img" aria-label="Shooting game in a train station" style="left:428px;top:14px;width:200px;height:112px;background:linear-gradient(180deg,#d8d6d0,#6b5a48)"></div>
    <div class="shot" role="img" aria-label="Person using a VR headset and controllers" style="left:15px;top:142px;width:93px;height:61px;background:linear-gradient(135deg,#1a2c4a,#5a7aa0)"></div>
    <div class="shot" role="img" aria-label="Woman wearing a VR headset" style="left:15px;top:219px;width:93px;height:56px;background:linear-gradient(135deg,#8a7a8c,#3a2c3a)"></div>
    <div class="shot" role="img" aria-label="Roller coaster between skyscrapers" style="left:124px;top:142px;width:249px;height:139px;background:linear-gradient(180deg,#4a8ad8,#2a3a4a 60%,#d0502a)"></div>
    <div class="shot" role="img" aria-label="Helicopter flight over icy landscape" style="left:386px;top:142px;width:242px;height:140px;background:linear-gradient(180deg,#5a6a80,#b8c0c8 55%,#4a5058)"></div>
    <div class="shot" role="img" aria-label="Dinosaur in a misty jungle" style="left:12px;top:297px;width:300px;height:168px;background:linear-gradient(135deg,#9aa8a0,#4a5448 60%,#2a302a)"></div>
    <div class="shot" role="img" aria-label="VR headset above a desert battle scene" style="left:328px;top:297px;width:300px;height:168px;background:linear-gradient(180deg,#c8c0b0,#b89a78)"></div>
  </section>

  <h3 class="headings">Fun for all ages</h3>
  <ul class="features">
    <li>Unique experience</li>
    <li>Immersive experience into 3D world</li>
    <li>Escape reality</li>
    <li>Be at heart of action - bottom of the ocean,</li>
    <li>travel the world, fight the invaders,</li>
    <li>solve the mystery and so much more</li>
    <li>System used is Brelvo Optra</li>
    <li>Dedicated room</li>
    <li>Family friendly</li>
  </ul>

  <h3 class="pricing">Pricing:</h3>
  <p class="price-line">$24 half hour.&nbsp; $40 per hour.</p>

  <p class="address">587 Larch Avenue<br>Three Hills, Alberta</p>
  <p class="contact"><span class="label">Contact:</span> 403-618-2093</p>
  <p class="brand">Termaldo<small>Technology Solutions</small></p>
</main>
</body>
</html>
```